Horse related business entrepreneur needs a business card

I need a business card design for my horse related business. The enterprise is Copper Vale LLC and I have 3 businesses (headquartered at 2 locations): 1. property management where we rent horse stalls and apartments at a thoroughbred training center outside Ocala; 2. a medium sized transportation service in central Florida that sells horse bedding and removes used horse bedding from horse farms; and horse racing

```html
<!DOCTYPE html>
<html lang="en">
<head>
<meta charset="utf-8">
<title>Copper Vale LLC — Business Card</title>
<link rel="stylesheet" href="https://fonts.googleapis.com/css2?family=Montserrat:wght@400;500;700;800&display=swap">
<style>
  :root {
    --copper: #7f4e36;
    --copper-light: #a0643e;
    --paper: #f7f7f7;
    --ink: #3c3c3c;
    --ink-soft: #6a6a6a;
    --rule: #bdbdbd;
    --backdrop: #ececec;
  }
  * { margin: 0; padding: 0; box-sizing: border-box; }
  html, body {
    width: 1200px; height: 1135px; overflow: hidden;
    background: var(--backdrop);
    font-family: "Montserrat", sans-serif;
  }
  .canvas {
    position: relative; width: 1200px; height: 1135px;
    display: flex; flex-direction: column; align-items: center; justify-content: center; gap: 70px;
  }
  .card {
    width: 770px; height: 440px;
    box-shadow: 0 8px 24px rgba(0,0,0,0.12);
    position: relative;
    overflow: hidden;
  }
  .card--front { background: var(--paper); display: flex; }
  .card--back { background: var(--copper); display: flex; flex-direction: column; align-items: center; justify-content: center; gap: 30px; }

  .brand { display: flex; flex-direction: column; align-items: flex-end; gap: 6px; }
  .brand__dot { width: 92px; height: 92px; border-radius: 50%; background: var(--copper); flex: none; margin-right: 10px; }
  .brand__name { font-weight: 800; font-size: 25px; letter-spacing: 0.5px; color: var(--copper); text-transform: uppercase; white-space: nowrap; }
  .card--back .brand__dot { background: var(--paper); width: 116px; height: 116px; margin-right: 20px; }
  .card--back .brand__name { color: var(--paper); font-size: 34px; }

  .front__brand-side { flex: 0 0 384px; display: flex; align-items: center; justify-content: center; }
  .front__divider { flex: 0 0 1px; background: var(--rule); margin: 110px 0; }
  .front__contact-side { flex: 1; padding: 0 0 0 54px; display: flex; flex-direction: column; justify-content: center; }

  .person__name { font-weight: 800; font-size: 30px; color: var(--ink); }
  .person__role { font-size: 17px; color: var(--ink-soft); margin-top: 2px; margin-bottom: 24px; }
  .contact-list { list-style: none; display: flex; flex-direction: column; gap: 7px; }
  .contact-list li { display: flex; align-items: center; gap: 12px; font-size: 19px; color: var(--ink); white-space: nowrap; }
  .contact-list svg { width: 17px; height: 17px; flex: none; fill: none; stroke: var(--copper-light); stroke-width: 1.8; }

  .addresses { text-align: center; color: var(--paper); font-size: 19px; font-weight: 500; line-height: 1.6; font-style: normal; }
</style>
</head>
<body>
<main class="canvas">
  <section class="card card--front">
    <div class="front__brand-side">
      <div class="brand">
        <span class="brand__dot"></span>
        <span class="brand__name">Copper Vale LLC</span>
      </div>
    </div>
    <div class="front__divider"></div>
    <div class="front__contact-side">
      <p class="person__name">Wade Thornton</p>
      <p class="person__role">Owner</p>
      <ul class="contact-list">
        <li><svg viewBox="0 0 20 20"><path d="M5 2 L8 2 L9 6 L7 8 Q9 12 12 13 L14 11 L18 12 L18 15 Q17 18 14 18 Q3 16 2 5 Q2 2 5 2 Z"/></svg>(555) 214-0187</li>
        <li><svg viewBox="0 0 20 20"><rect x="2" y="6" width="16" height="11" rx="1.5"/><path d="M7 6 V3.5 H13 V6"/></svg>(555) 382-0916</li>
        <li><svg viewBox="0 0 20 20"><rect x="2" y="4" width="16" height="12" rx="1"/><path d="M2 4 L10 11 L18 4"/></svg>wade@coppervale.com</li>
        <li><svg viewBox="0 0 20 20"><circle cx="10" cy="10" r="8"/><ellipse cx="10" cy="10" rx="3.5" ry="8"/><path d="M2 10 H18"/></svg>www.coppervale.com</li>
      </ul>
    </div>
  </section>

  <section class="card card--back">
    <div class="brand">
      <span class="brand__dot"></span>
      <span class="brand__name">Copper Vale LLC</span>
    </div>
    <address class="addresses">
      1250 SE Meadow Lane, Fairfield, FL 32600<br>
      780 Willow Creek Road, Ashford, VA 22900
    </address>
  </section>
</main>
</body>
</html>
```